" Empresa que trabalha com danças urbanas. Workhops, Batalhas, Performances, Palestras, Bate-papos, Jam Sessions. Também possui um projeto social em comunidades. "

```html
<!DOCTYPE html>
<html lang="pt-BR">
<head>
<meta charset="utf-8">
<title>Ritmo Urbano — Novidades</title>
<link href="https://fonts.googleapis.com/css2?family=Oswald:wght@400;600;700&family=Open+Sans:wght@400;600&display=swap" rel="stylesheet">
<style>
:root{
  --page-bg:#ffffff;
  --body-dark:#262626;
  --body-mid:#333333;
  --card:#3b3b3b;
  --card-edge:#4a4a4a;
  --silver-light:#e4e4e4;
  --silver-dark:#a9a9a9;
  --text-light:#f2f2f2;
  --text-muted:#b5b5b5;
  --text-dark:#222222;
  --accent-yellow:#f2d21b;
  --accent-green:#4a7a1e;
  --photo-a:#6f6478;
  --photo-b:#c9b9a6;
}
*{box-sizing:border-box;margin:0;padding:0}
html,body{width:1200px;height:1200px;overflow:hidden;background:var(--page-bg);font-family:"Open Sans",Arial,sans-serif}
.site{position:absolute;left:67px;top:0;width:1066px;height:1200px;background:linear-gradient(180deg,var(--body-mid),var(--body-dark) 40%,var(--body-mid));}
.top-stripe{height:6px;background:linear-gradient(90deg,var(--accent-green),var(--accent-yellow) 50%,var(--accent-green))}
.header{position:relative;height:104px;background:linear-gradient(180deg,#1c1c1c,#3a3a3a)}
.flags{position:absolute;left:250px;top:30px;display:flex;gap:6px}
.flag{width:26px;height:17px;border-radius:2px}
.flag.br{background:#2f8a3b}
.flag.us{background:#8c8fa8}
.newsletter{position:absolute;left:438px;top:14px;width:186px;height:66px;background:linear-gradient(180deg,#f4f4f4,#cfcfcf);border-radius:3px;text-align:center;padding-top:8px;font-size:11px;color:var(--text-dark);line-height:14px}
.newsletter strong{font-weight:600}
.newsletter .btn{display:inline-block;margin-top:5px;background:#2b2b2b;color:var(--text-light);font:600 9px "Oswald",sans-serif;padding:2px 9px;letter-spacing:.5px}
.social-top{position:absolute;left:660px;top:40px;display:flex;gap:4px}
.social-top span{width:16px;height:16px;background:#cfcfcf;border-radius:2px}
.social-top span.wide{width:40px}
.brand{position:absolute;right:30px;top:34px;display:flex;align-items:center;gap:8px;font:700 20px "Oswald",sans-serif;color:var(--text-light)}
.brand i{width:14px;height:14px;background:var(--text-light);border-radius:50%}
.nav{height:32px;background:linear-gradient(180deg,var(--silver-light),var(--silver-dark));display:flex;justify-content:center;align-items:center;gap:22px;font:600 12px "Oswald",sans-serif;color:var(--text-dark)}
.nav .active{color:#000;border-bottom:2px solid #000}
.subnav{height:22px;background:linear-gradient(90deg,#222,var(--accent-green) 30%,#3d5a1d 70%,#222);display:flex;justify-content:center;align-items:center;gap:40px;font-size:11px;color:#e8e8c8;padding-right:80px}
.subnav .active{color:#fff;font-weight:600}
.section-title{position:absolute;left:305px;top:204px;width:456px;height:46px;background:linear-gradient(180deg,#f0f0f0,#b9b9b9);display:flex;justify-content:center;align-items:center;font:700 22px "Oswald",sans-serif;color:var(--text-dark);letter-spacing:.5px;clip-path:polygon(0 0,100% 0,97% 100%,0 100%)}
.grid{position:absolute;left:34px;top:300px;display:grid;grid-template-columns:repeat(5,182px);column-gap:10px;row-gap:24px}
.card{height:288px;background:var(--card);border:1px solid var(--card-edge);padding:14px 10px 0;text-align:center}
.card .photo{height:142px;margin:0 2px;background:linear-gradient(135deg,var(--photo-a),var(--photo-b))}
.card .photo.group{background:linear-gradient(135deg,#d8d8d8,#6a6a6a)}
.card h3{font:400 13px/17px "Oswald",sans-serif;color:var(--text-light);margin-top:12px;height:36px;display:flex;align-items:center;justify-content:center;overflow:hidden}
.card .rule{border-top:3px dotted #9a9a9a;margin:8px 0 9px}
.card p{font-size:10px;line-height:13px;color:var(--text-muted)}
.pager{position:absolute;left:0;right:0;top:946px;display:flex;justify-content:center;gap:6px}
.pager span{width:14px;height:14px;background:#6a6a6a}
.pager span.arrow{background:#d9d9d9}
.to-top{position:absolute;right:30px;top:936px;width:40px;height:40px;background:#dcdcdc;border-radius:3px}
.footer-band{position:absolute;left:0;right:0;top:1003px;height:28px;background:linear-gradient(180deg,var(--silver-light),var(--silver-dark));display:flex;justify-content:center;align-items:center;gap:4px}
.footer-band span{width:16px;height:16px;background:#333;border-radius:2px}
.follow{position:absolute;left:0;right:0;top:1038px;text-align:center;font-size:10px;color:var(--text-light)}
.widget{position:absolute;left:456px;top:1056px;width:154px;height:106px;background:#f4f4f4;padding:6px}
.widget .name{font-size:9px;font-weight:600;color:var(--text-dark);display:flex;align-items:center;gap:4px}
.widget .name i{width:14px;height:14px;background:#333}
.widget .thumbs{margin-top:8px;height:68px;background:linear-gradient(90deg,#8a7a6a,#bdb3a5,#6a6a7a)}
.copyright{position:absolute;left:0;right:0;bottom:0;height:28px;background:linear-gradient(180deg,#d8d8d8,#b0b0b0);font-size:9px;color:#444;display:flex;align-items:center;justify-content:center}
</style>
</head>
<body>
<div class="site">
  <div class="top-stripe"></div>
  <header class="header">
    <div class="flags"><span class="flag br" role="img" aria-label="Bandeira do Brasil"></span><span class="flag us" role="img" aria-label="Bandeira dos Estados Unidos"></span></div>
    <div class="newsletter">Saiba de tudo que<br>rola na <strong>Ritmo Urbano</strong><br><span class="btn">CADASTRE-SE</span></div>
    <div class="social-top"><span class="wide"></span><span></span><span></span><span></span><span></span></div>
    <div class="brand"><i></i>Ritmo Urbano</div>
  </header>
  <nav class="nav"><span>HOME</span><span class="active">SOBRE</span><span>EVENTOS</span><span>PROJETO SOCIAL</span><span>PARCEIROS</span><span>CURADORIA</span><span>EQUIPE</span><span>SHOP</span><span>NEWS</span><span>CONTATO</span></nav>
  <div class="subnav"><span class="active">Apresentação</span><span>Festival 2015</span><span>Festival 2014</span><span>Festival 2013</span></div>

  <h2 class="section-title">NOVIDADES</h2>

  <div class="grid">
    <article class="card"><div class="photo group" role="img" aria-label="Foto de dançarinos em workshop"></div><h3>RITMO URBANO - WORKSHOPS EM MINAS GERAIS</h3><div class="rule"></div><p>Minas Gerais recebe artistas cariocas de vários estilos no fim de semana...</p></article>
    <article class="card"><div class="photo" role="img" aria-label="Foto de crianças do projeto social"></div><h3>O PROJETO PASSOS DA RUA CAMINHANDO E CRESCENDO</h3><div class="rule"></div><p>Minas Gerais recebe artistas cariocas de vários estilos no fim de semana...</p></article>
    <article class="card"><div class="photo" role="img" aria-label="Foto de crianças do projeto social"></div><h3>O PROJETO PASSOS DA RUA CAMINHANDO E CRESCENDO</h3><div class="rule"></div><p>Minas Gerais recebe artistas cariocas de vários estilos no fim de semana...</p></article>
    <article class="card"><div class="photo" role="img" aria-label="Foto de crianças do projeto social"></div><h3>O PROJETO PASSOS DA RUA CAMINHANDO E CRESCENDO</h3><div class="rule"></div><p>Minas Gerais recebe artistas cariocas de vários estilos no fim de semana...</p></article>
    <article class="card"><div class="photo" role="img" aria-label="Foto de crianças do projeto social"></div><h3>O PROJETO PASSOS DA RUA CAMINHANDO E CRESCENDO</h3><div class="rule"></div><p>Minas Gerais recebe artistas cariocas de vários estilos no fim de semana...</p></article>
    <article class="card"><div class="photo" role="img" aria-label="Foto de crianças do projeto social"></div><h3>O PROJETO PASSOS DA RUA CAMINHANDO E CRESCENDO</h3><div class="rule"></div><p>Minas Gerais recebe artistas cariocas de vários estilos no fim de semana...</p></article>
    <article class="card"><div class="photo" role="img" aria-label="Foto de crianças do projeto social"></div><h3>O PROJETO PASSOS DA RUA CAMINHANDO E CRESCENDO</h3><div class="rule"></div><p>Minas Gerais recebe artistas cariocas de vários estilos no fim de semana...</p></article>
    <article class="card"><div class="photo" role="img" aria-label="Foto de crianças do projeto social"></div><h3>O PROJETO PASSOS DA RUA CAMINHANDO E CRESCENDO</h3><div class="rule"></div><p>Minas Gerais recebe artistas cariocas de vários estilos no fim de semana...</p></article>
    <article class="card"><div class="photo" role="img" aria-label="Foto de crianças do projeto social"></div><h3>O PROJETO PASSOS DA RUA CAMINHANDO E CRESCENDO</h3><div class="rule"></div><p>Minas Gerais recebe artistas cariocas de vários estilos no fim de semana...</p></article>
    <article class="card"><div class="photo" role="img" aria-label="Foto de crianças do projeto social"></div><h3>O PROJETO PASSOS DA RUA CAMINHANDO E CRESCENDO</h3><div class="rule"></div><p>Minas Gerais recebe artistas cariocas de vários estilos no fim de semana...</p></article>
  </div>

  <div class="pager"><span class="arrow"></span><span class="arrow"></span><span></span><span></span><span></span><span></span><span></span><span></span><span></span><span></span><span class="arrow"></span><span class="arrow"></span></div>
  <div class="to-top" aria-label="Voltar ao topo">
    <svg width="40" height="40" viewBox="0 0 40 40"><path d="M12 24 L20 16 L28 24" fill="none" stroke="#222" stroke-width="3"/></svg>
  </div>

  <div class="footer-band"><span></span><span></span><span></span><span></span></div>
  <p class="follow">Acompanhe a Ritmo Urbano nas redes sociais!</p>
  <div class="widget">
    <div class="name"><i></i>Ritmo Urbano</div>
    <div class="thumbs" role="img" aria-label="Miniaturas de fotos dos seguidores"></div>
  </div>
  <footer class="copyright">Copyright © 2013 Ritmo Urbano · Todos os direitos reservados</footer>
</div>
</body>
</html>
```